Consulting Practice for Charities Needs A Brochure Deisgn

Hi! We need a tri-fold brochure for a Washington, DC based consulting practice that works with charities (NGOs, Associations, etc.) and wealthy donors (philanthropists). Our company, Brennick Civic Advisors, helps nonprofits to implement practices that maximize organizational efficiency and effectiveness - by working directly with board members and staff.
Our clients are well educated and quite sophisticated (some charities are international with multi-million dollar budgets, while others are quite local and small) This brochure will be handed to them by some of our 'referral partners' (law firms, accountants and even governmental agencies) in addition to being given out during our presentations. We draw inspiration from nature and would like to somehow include a "natural / eco-friendly" feel to the piece, including natural colors .... that being said, not in any way "folksy" - it must be sophisticated.

Target Market(s)

nonprofit executive directors, board chairs, wealth holders (philanthropists)

Industry/Entity Type

Consulting

Requirements
Must have
• I uploaded a word file with content (text) - most of that needs to be on the brochure ... but ... if it looks too crowded, let me know and I'll reduce
Nice to have
• pop-out quotes (maybe from testimonials??), nature - theme of some kind but also photo of boardroom (links to samples are like are uploaded in a word doc below)
Should not have
• nothing cute ... nothing too feminine

```html
<!DOCTYPE html>
<html lang="en">
<head>
<meta charset="utf-8">
<title>Brennick Civic Advisors – Tri-fold Brochure</title>
<link href="https://fonts.googleapis.com/css2?family=Montserrat:ital,wght@0,400;0,600;0,700;0,800;1,700&family=Open+Sans:wght@400;600&display=swap" rel="stylesheet">
<style>
  :root{
    --purple:#6b5ba6;
    --purple-deep:#55478f;
    --lavender:#b9b0da;
    --lavender-pale:#e4e0f2;
    --navy:#262a44;
    --ink:#4a4a55;
    --paper:#ffffff;
    --gap:#eef0f3;
  }
  *{box-sizing:border-box;margin:0;padding:0}
  html,body{width:851px;height:1200px;overflow:hidden;background:var(--gap)}
  .canvas{position:relative;width:851px;height:1200px;overflow:hidden;font-family:"Open Sans",Arial,sans-serif;color:var(--ink)}
  .sheet{position:absolute;left:0;width:851px;height:592px;background:var(--paper);overflow:hidden}
  .sheet--outside{top:0}
  .sheet--inside{top:608px}
  .shapes{position:absolute;inset:0;width:100%;height:100%}
  .panel{position:absolute;top:0;width:283px;height:592px}
  .panel--left{left:0}
  .panel--mid{left:284px}
  .panel--right{left:568px}
  .photo{position:absolute}
  .heading{font-family:"Montserrat",sans-serif;font-weight:700;color:var(--purple);letter-spacing:.5px;text-transform:uppercase}
  .small{font-size:6.6px;line-height:1.45}
  .small p{margin-bottom:5px}
  .attrib{font-weight:600;color:var(--purple)}
  .badge{position:absolute;background:var(--lavender-pale);border:1px solid var(--lavender)}
  .inquire{position:absolute;left:0;width:283px;top:196px;text-align:center;font-family:"Montserrat",sans-serif;font-weight:700;color:var(--navy);font-size:11px;line-height:1.5;letter-spacing:.3px}
  .contact{position:absolute;left:0;width:283px;top:280px;text-align:center;font-family:"Montserrat",sans-serif;font-weight:600;color:var(--navy);font-size:7px;line-height:1.7}
  .callus{position:absolute;left:0;width:283px;top:314px;text-align:center;font-family:"Montserrat",sans-serif;font-weight:800;color:var(--navy);font-size:16px;letter-spacing:.3px}
  .brand{position:absolute;left:40px;top:228px;width:210px;display:flex;align-items:center;gap:10px}
  .brand-square{width:22px;height:22px;background:var(--purple);flex:none}
  .brand-name{font-family:"Montserrat",sans-serif;font-weight:700;color:var(--purple);font-size:21px;line-height:1.15}
  .list-caps{font-family:"Montserrat",sans-serif;font-size:5.8px;font-weight:600;line-height:1.6;color:var(--ink);list-style:none}
  .list-caps li::before{content:"■ ";color:var(--purple)}
  .methods{font-family:"Montserrat",sans-serif;font-style:italic;font-weight:700;color:var(--purple);font-size:12.5px;line-height:1.3;text-align:center}
  .lead{font-family:"Montserrat",sans-serif;font-weight:700;color:var(--purple);font-size:14px;line-height:1.3;text-align:center}
  .services{text-align:center;font-size:6.6px;line-height:1.65}
  .services b{font-family:"Montserrat",sans-serif;color:var(--navy);font-weight:700}
</style>
</head>
<body>
<div class="canvas">

  <!-- OUTSIDE SHEET -->
  <section class="sheet sheet--outside">
    <svg class="shapes" viewBox="0 0 851 592" aria-hidden="true">
      <polygon points="0,0 70,0 0,55" fill="var(--lavender)"/>
      <polygon points="0,420 0,592 90,592" fill="var(--purple)"/>
      <polygon points="200,470 283,400 283,592 150,592" fill="var(--lavender)"/>
      <polygon points="284,592 284,480 400,592" fill="var(--lavender)"/>
      <polygon points="360,592 520,440 567,440 567,592" fill="var(--purple)"/>
      <polygon points="470,592 567,500 567,592" fill="var(--navy)"/>
      <polygon points="568,0 640,0 568,90" fill="var(--purple)"/>
      <polygon points="568,592 568,470 700,592" fill="var(--purple)"/>
      <line x1="590" y1="300" x2="830" y2="300" stroke="var(--purple)" stroke-width="1.5"/>
    </svg>

    <div class="panel panel--left">
      <h2 class="heading" style="position:absolute;left:20px;top:18px;font-size:17px">Testimonials</h2>
      <div class="small" style="position:absolute;left:20px;top:46px;width:245px">
        <p class="attrib">Executive Director, Riverside Land Trust</p>
        <p>"Their counsel reshaped how our board works with staff. Meetings are focused, roles are clear, and our strategy finally reflects our mission. We could not have made this change without their steady guidance."</p>
      </div>
      <div class="photo" role="img" aria-label="Photo of a board meeting around a conference table"
           style="left:0;top:140px;width:240px;height:175px;background:linear-gradient(135deg,#c9c6cf,#8d8a98 55%,#5d5a6c);clip-path:polygon(0 0,85% 0,100% 100%,0 100%)"></div>
      <div class="small" style="position:absolute;left:20px;top:328px;width:245px">
        <p class="attrib">Board Chair, Harbor Arts Alliance</p>
        <p>"A thoughtful and candid partner. The assessment gave our directors a shared picture of where we stand and a practical plan for growth over the next three years."</p>
      </div>
      <div class="photo" role="img" aria-label="Photo of colleagues working together"
           style="left:40px;top:440px;width:190px;height:152px;background:linear-gradient(160deg,#a9a6b4,#6e6b7d);clip-path:polygon(30% 0,100% 0,75% 100%,0 100%)"></div>
    </div>

    <div class="panel panel--mid">
      <div class="badge" style="left:126px;top:14px;width:30px;height:20px;border-radius:3px"></div>
      <div class="badge" style="left:108px;top:44px;width:66px;height:26px"></div>
      <div class="badge" style="left:116px;top:82px;width:50px;height:40px;border-radius:4px"></div>
      <svg style="position:absolute;left:129px;top:164px" width="26" height="26" aria-hidden="true"><circle cx="13" cy="13" r="12" fill="var(--purple)"/></svg>
      <div class="inquire">INQUIRE ABOUT A<br>COMPLIMENTARY EVALUATION<br>PACKAGES AVAILABLE</div>
      <div class="contact">info@brennickcivic.com<br>www.brennickcivic.com</div>
      <div class="callus">CALL US: +1.301.555.0148</div>
    </div>

    <div class="panel panel--right">
      <div class="photo" role="img" aria-label="Photo of a professional meeting"
           style="left:60px;top:0;width:223px;height:150px;background:linear-gradient(135deg,#d5d3dc,#9996a6);clip-path:polygon(30% 0,100% 0,100% 100%,0 100%)"></div>
      <div class="brand">
        <span class="brand-square"></span>
        <span class="brand-name">Brennick Civic Advisors</span>
      </div>
      <div class="photo" role="img" aria-label="Photo of advisors reviewing documents"
           style="left:70px;top:420px;width:213px;height:172px;background:linear-gradient(160deg,#b5b2c0,#6f6c80);clip-path:polygon(40% 0,100% 0,100% 100%,0 100%)"></div>
    </div>
  </section>

  <!-- INSIDE SHEET -->
  <section class="sheet sheet--inside">
    <svg class="shapes" viewBox="0 0 851 592" aria-hidden="true">
      <polygon points="0,0 45,0 0,45" fill="var(--purple)"/>
      <polygon points="0,592 0,520 70,592" fill="var(--purple)"/>
      <polygon points="480,0 567,0 567,80" fill="var(--lavender)"/>
      <polygon points="520,0 567,0 567,40" fill="var(--purple)"/>
      <polygon points="568,95 851,60 851,110 568,145" fill="var(--purple)"/>
      <polygon points="568,592 568,470 680,592" fill="var(--purple)"/>
    </svg>

    <div class="panel panel--left">
      <h2 class="heading" style="position:absolute;left:22px;top:16px;font-size:12px;color:var(--navy)">Who We Are</h2>
      <div class="small" style="position:absolute;left:22px;top:36px;width:240px">
        <p>Brennick Civic Advisors is a Washington, DC practice that guides nonprofit boards, executives and philanthropists toward sound governance and lasting impact.</p>
        <p>Our principals bring decades of leadership across associations, foundations and international NGOs, pairing research with practical, hands-on support.</p>
        <p><b>WE WORK WITH ORGANIZATIONS THAT WISH TO:</b></p>
      </div>
      <ul class="list-caps" style="position:absolute;left:22px;top:128px;width:240px">
        <li>Strengthen board and staff partnership</li>
        <li>Clarify roles and responsibilities</li>
        <li>Build a focused strategic plan</li>
        <li>Improve board recruitment and renewal</li>
        <li>Prepare for leadership transition</li>
        <li>Measure results and report impact</li>
      </ul>
      <h2 class="heading" style="position:absolute;left:22px;top:250px;font-size:12px;color:var(--navy)">What We Do</h2>
      <div class="small" style="position:absolute;left:22px;top:270px;width:240px">
        <p>We assess how your organization governs and operates, then design tailored steps that raise efficiency and effectiveness. Engagements range from a single retreat to multi-year advisory support.</p>
        <p>Every plan is built with your board and staff, so the changes hold long after our work is done.</p>
      </div>
      <p class="methods" style="position:absolute;left:24px;top:400px;width:236px">Our methods are informed by research and honed by over 20 years of practice.</p>
    </div>

    <div class="panel panel--mid">
      <h2 class="heading" style="position:absolute;left:0;width:283px;text-align:center;top:18px;font-size:8px">Private Clients</h2>
      <p class="lead" style="position:absolute;left:25px;top:34px;width:233px">BCA philanthropic counsel helps individuals adopt impactful practices in their charitable</p>
      <h2 class="heading" style="position:absolute;left:0;width:283px;text-align:center;top:128px;font-size:11px">Our Services</h2>
      <div class="services" style="position:absolute;left:20px;top:148px;width:243px">
        <b>Board and Senior Staff Coaching</b><br>
        Workshops, Seminars and Retreat Including<br>
        Roles &amp; Responsibilities<br>
        Fundraising<br>
        Governance Planning<br>
        Board Self-Assessments<br>
        Strategic Planning<br>
        Board Recruitment Training<br>
        Committee Development<br>
        Bylaws &amp; Policy Review<br><br>
        <b>Philanthropic Counsel</b><br>
        Giving Strategy<br>
        Family Foundation Setup<br>
        Grant Review &amp; Evaluation
      </div>
    </div>

    <div class="panel panel--right">
      <div class="small" style="position:absolute;left:20px;top:16px;width:245px">
        <p class="attrib">President, Lakeshore Food Network</p>
        <p>"Their team helped us rebuild our board committees and sharpen our strategy. Staff and directors now pull in the same direction."</p>
      </div>
      <div class="small" style="position:absolute;left:20px;top:150px;width:245px">
        <p class="attrib">Donor, Family Giving Fund</p>
        <p>"I came looking for a clear giving plan and left with a framework my family will use for years. Practical, discreet and genuinely insightful counsel."</p>
      </div>
      <h2 class="heading" style="position:absolute;right:22px;top:232px;font-size:15px">Testimonials</h2>
      <div class="photo" role="img" aria-label="Photo of a consultant meeting with a client at a desk"
           style="left:0;top:270px;width:283px;height:322px;background:linear-gradient(150deg,#dcd6cd,#b4aa9c 50%,#8a8174)"></div>
      <svg style="position:absolute;left:0;top:470px" width="120" height="122" aria-hidden="true"><polygon points="0,0 0,122 112,122" fill="var(--purple)"/></svg>
    </div>
  </section>

</div>
</body>
</html>
```